Kestrel Summit 2019 Enemies of the End-Times Church Flyer

We want a church conference flyer designed. We are looking for a professional, yet catchy design that uses our brand colors and logo creatively while communicating key information of the event effectively. <br/>The flyer must include all of the following:<br/>Title: Kestrel Summit 2019<br/>Topic: The Enemies of The End-Times Church <br/>Subtitles: <br/> -How the antichrist raises an army by social behavior engineering. <br/>-How the architects of modern social constructs escaped the church's radar. <br/>-The Holy Spirit's end-times agenda:<br/> The Knock-Out Punch!<br/>Speaker: Prophet Marcus Toliver <br/>Dates/time: December 27, 28 & 29 at 6pm<br/>Location: Halvorn Community Center <br/> 241 Pellham Street <br/> Portland, ME 04102<br/>Contact info: phone: 207-555-0148 <br/>email: contact@brookmeadow.example <br/> www.vutel.example<br/>*The flyer must also include a picture of the speaker and our Vutel logo <br/>Thanks, we look forward to seeing what you come up with!

Colors

Designer to choose colors to be used in the design.

Requirements
Must have
• The flyer must include all of the following:
• Title: Kestrel Summit 2019
• Topic: The Enemies of The End-Times Church
• Subtitles:
• -How the antichrist raises an army by social behavior engineering.
• -How the architects of modern social constructs escaped the church's radar.
• -The Holy Spirit's end-times agenda:
• The Knock-Out Punch!
• Speaker: Prophet Marcus Toliver
• Dates/time: December 27, 28 & 29 at 6pm
• Location: Halvorn Community Center
• 241 Pellham Street
• Portland, ME 04102
• Contact info: phone: 207-555-0148
• email: contact@brookmeadow.example
• www.vutel.example
• *The flyer must also include a picture of the speaker and our Vutel logo
Should not have
• Pictures of crosses or church buildings

```html
<!DOCTYPE html>
<html lang="en">
<head>
<meta charset="utf-8">
<title>Kestrel Summit 2019 Flyer</title>
<link rel="stylesheet" href="https://fonts.googleapis.com/css2?family=Anton&family=Fira+Sans+Condensed:wght@400;500;600&family=Roboto:wght@400&display=swap">
<style>
  :root {
    --orange-deep: #e25a10;
    --orange: #f0901f;
    --orange-warm: #f4a12e;
    --rust: #a34e1d;
    --navy: #0d3153;
    --navy-panel: #114471;
    --navy-text: #163a63;
    --gold: #f2ae0c;
    --pale-yellow: #f6f38e;
    --speaker-orange: #f3a21f;
    --ink: #1c1c1c;
    --paper-top: #f6f7f9;
    --paper-bottom: #dde2ea;
    --white: #ffffff;
  }
  * { margin: 0; padding: 0; box-sizing: border-box; }
  html, body { width: 849px; height: 1200px; overflow: hidden; background: var(--white); }
  .flyer {
    position: relative; width: 849px; height: 1200px; overflow: hidden;
    background: linear-gradient(180deg, var(--paper-top) 55%, var(--paper-bottom) 100%);
    font-family: "Fira Sans Condensed", sans-serif;
  }
  .backdrop { position: absolute; inset: 0; }
  .speaker-hero {
    position: absolute; left: 60px; top: 50px; width: 690px; height: 480px;
    background: radial-gradient(ellipse 50% 52% at 48% 50%, rgba(205,190,175,0.95) 0%, rgba(170,150,130,0.75) 40%, rgba(240,150,50,0) 75%);
  }
  .brand-box {
    position: absolute; left: 642px; top: 38px; width: 178px; height: 178px;
    background: var(--navy);
    display: flex; align-items: center; justify-content: center;
  }
  .brand-name { color: var(--white); font-weight: 500; font-size: 44px; letter-spacing: 1px; }
  .event-title {
    position: absolute; left: 78px; top: 424px; white-space: nowrap;
    font-family: "Anton", sans-serif; font-weight: 400; font-size: 83px; line-height: 1; color: #0a0a0a;
    -webkit-text-stroke: 4px var(--white); paint-order: stroke fill; letter-spacing: 0.3px;
  }
  .event-topic {
    position: absolute; left: 81px; top: 537px;
    font-weight: 600; font-size: 32px; line-height: 40px; color: var(--ink);
  }
  .talks { position: absolute; left: 81px; top: 690px; width: 337px; list-style: none; border-top: 2px solid var(--orange); }
  .talks li {
    font-size: 22.5px; line-height: 29px; color: var(--ink); white-space: nowrap;
    padding: 6px 0 5px; border-bottom: 2px solid var(--orange);
  }
  .detail { position: absolute; left: 81px; display: flex; align-items: center; gap: 13px; color: var(--ink); }
  .detail svg { flex: none; }
  .detail-date { top: 916px; }
  .date-month { font-weight: 500; font-size: 23px; line-height: 22px; }
  .date-days { font-weight: 600; font-size: 37px; line-height: 38px; }
  .date-days small { font-size: 22px; font-weight: 500; }
  .detail-venue { top: 1010px; }
  .venue-text { font-weight: 600; font-size: 23.5px; line-height: 29px; color: #18202b; white-space: nowrap; }
  .session-panel {
    position: absolute; left: 443px; top: 553px; width: 377px; height: 457px;
    background: var(--gold); border-top-left-radius: 34px;
  }
  .session-panel-inner {
    position: absolute; left: 15px; top: 0; right: 0; bottom: 0;
    background: linear-gradient(180deg, var(--navy-panel), var(--navy));
    border-top-left-radius: 30px; text-align: center; color: var(--white);
  }
  .session-heading { color: var(--pale-yellow); font-weight: 600; font-size: 34px; line-height: 36px; padding-top: 26px; }
  .session-heading span { display: block; font-size: 42px; line-height: 44px; }
  .speaker-portrait {
    position: absolute; left: 97px; top: 114px; width: 169px; height: 233px;
    border: 1px solid #6b8fb5;
    background: linear-gradient(180deg, #b9b3aa 0%, #8a7d74 45%, #3b3b40 75%, #2b2b30 100%);
    box-shadow: 6px 8px 14px rgba(0,0,0,0.35);
  }
  .speaker-label { position: absolute; left: 0; right: 0; top: 368px; font-family: "Roboto", sans-serif; font-size: 21px; }
  .speaker-name { position: absolute; left: 0; right: 0; top: 398px; color: var(--speaker-orange); font-weight: 600; font-size: 33px; white-space: nowrap; }
  .contact-bar {
    position: absolute; left: 0; right: 0; top: 1132px; height: 44px;
    color: var(--navy-text); font-weight: 500; font-size: 24px;
  }
  .contact-item { position: absolute; top: 0; height: 44px; display: flex; align-items: center; gap: 10px; white-space: nowrap; }
  .contact-item svg { flex: none; }
  .contact-phone { left: 40px; }
  .contact-mail { left: 246px; font-size: 20px; }
  .contact-web { left: 600px; }
</style>
</head>
<body>
<main class="flyer">
  <svg class="backdrop" width="849" height="1200" viewBox="0 0 849 1200" aria-hidden="true">
    <defs>
      <linearGradient id="heroGlow" x1="0" y1="0" x2="1" y2="0.6">
        <stop offset="0" stop-color="var(--orange-deep)"/>
        <stop offset="0.55" stop-color="var(--orange)"/>
        <stop offset="0.85" stop-color="var(--orange-warm)"/>
        <stop offset="1" stop-color="var(--rust)"/>
      </linearGradient>
    </defs>
    <path d="M0 0 H849 V651 H96 Q14 651 0 588 Z" fill="var(--navy)"/>
    <path d="M0 0 H849 V633 H96 Q22 633 0 570 Z" fill="url(#heroGlow)"/>
    <path d="M0 1095 H790 Q846 1095 849 1145 V1200 H0 Z" fill="var(--navy)"/>
    <path d="M0 1106 H786 Q836 1106 849 1160 V1200 H0 Z" fill="var(--orange)"/>
  </svg>

  <div class="speaker-hero" role="img" aria-label="Photo of the speaker preaching with a headset microphone"></div>

  <div class="brand-box"><span class="brand-name">Vutel</span></div>

  <h1 class="event-title">Kestrel Summit 2019</h1>
  <p class="event-topic">The Enemies of<br>The End-Times Church</p>

  <ul class="talks">
    <li>How the antichrist raises an army by<br>social behavior engineering</li>
    <li>How the architects of modern social<br>constructs escaped the church's radar</li>
    <li>The Holy Spirit's end-times agenda</li>
  </ul>

  <div class="detail detail-date">
    <svg width="44" height="53" viewBox="0 0 44 53" fill="none" stroke="var(--navy-panel)" stroke-width="3" stroke-linecap="round">
      <rect x="2" y="6" width="40" height="44" rx="6"/>
      <path d="M11 2 V10 M22 2 V10 M33 2 V10"/>
      <g fill="var(--navy-panel)" stroke="none">
        <circle cx="11" cy="22" r="1.8"/><circle cx="19" cy="22" r="1.8"/><circle cx="27" cy="22" r="1.8"/>
        <circle cx="11" cy="30" r="1.8"/><circle cx="19" cy="30" r="1.8"/>
        <circle cx="11" cy="38" r="1.8"/><circle cx="19" cy="38" r="1.8"/>
      </g>
      <circle cx="33" cy="40" r="9" fill="var(--paper-top)"/>
      <path d="M33 35 V40 H37"/>
    </svg>
    <div>
      <div class="date-month">December</div>
      <div class="date-days">27, 28 <small>&amp;</small> 29 <small>at</small> 6<small>pm</small></div>
    </div>
  </div>

  <div class="detail detail-venue">
    <svg width="41" height="54" viewBox="0 0 41 54">
      <path d="M20.5 0 C9 0 0 9 0 20.5 C0 34 20.5 54 20.5 54 C20.5 54 41 34 41 20.5 C41 9 32 0 20.5 0 Z" fill="var(--navy-panel)"/>
      <circle cx="20.5" cy="19.5" r="7.5" fill="var(--paper-top)"/>
    </svg>
    <div class="venue-text">Halvorn Community Center<br>241 Pellham Street Portland, ME 04102</div>
  </div>

  <section class="session-panel">
    <div class="session-panel-inner">
      <h2 class="session-heading">The<span>Knock-Out Punch!</span></h2>
      <div class="speaker-portrait" role="img" aria-label="Portrait of the speaker seated in front of a bookshelf"></div>
      <p class="speaker-label">Speaker</p>
      <p class="speaker-name">Prophet Marcus Toliver</p>
    </div>
  </section>

  <footer class="contact-bar">
    <div class="contact-item contact-phone">
      <svg width="30" height="30" viewBox="0 0 24 24"><path fill="var(--white)" d="M6.6 10.8a15.1 15.1 0 0 0 6.6 6.6l2.2-2.2c.3-.3.7-.4 1-.2 1.1.4 2.3.6 3.6.6.6 0 1 .4 1 1V20c0 .6-.4 1-1 1A17 17 0 0 1 3 4c0-.6.4-1 1-1h3.5c.6 0 1 .4 1 1 0 1.3.2 2.5.6 3.6.1.3 0 .7-.2 1z"/></svg>
      <span>207 555 0148</span>
    </div>
    <div class="contact-item contact-mail">
      <svg width="34" height="24" viewBox="0 0 34 24" fill="none" stroke="var(--white)" stroke-width="2.5"><rect x="1.5" y="1.5" width="31" height="21"/><path d="M1.5 1.5 L17 14 L32.5 1.5 M1.5 22.5 L13 11 M32.5 22.5 L21 11"/></svg>
      <span>contact@brookmeadow.example</span>
    </div>
    <div class="contact-item contact-web">
      <svg width="38" height="38" viewBox="0 0 38 38" fill="none" stroke="var(--white)" stroke-width="2.5"><circle cx="19" cy="19" r="16.5"/><ellipse cx="19" cy="19" rx="7" ry="16.5"/><path d="M2.5 19 H35.5 M5 11 H33 M5 27 H33 M19 2.5 V35.5"/></svg>
      <span>www.vutel.example</span>
    </div>
  </footer>
</main>
</body>
</html>
```